Calloway needs a modernized design

We would like a modern update (that can be responsive) to our existing website. Attached are the two existing pages we would like new concepts of - our home page and a page about one of our locations.

Calloway is provides executive offices and virtual office services. Startups, law firms, and financial services are our primary clients. We would like a professional, clean design, leaning towards minimalist. We intend to greatly reduce/eliminate the long paragraphs of text.

Industry/Entity Type

Business Service

Number of Pages Required

2 page

Requirements
Must have
• A design that can be responsive
Nice to have
• Large image(s) on home page that rotate.

```html
<!DOCTYPE html>
<html lang="en">
<head>
<meta charset="utf-8">
<title>Calloway Business Centers</title>
<link href="https://fonts.googleapis.com/css2?family=Figtree:wght@400;500;600;700&display=swap" rel="stylesheet">
<style>
:root{
  --navy:#2b3b50;
  --ink:#24344a;
  --text:#555b63;
  --muted:#8a9097;
  --teal:#1fbf9b;
  --line:#e4e6e8;
  --soft:#f7f7f7;
  --white:#ffffff;
  --gold:#f2c230;
  --sky:#2a9bd8;
}
*{box-sizing:border-box;margin:0;padding:0}
html,body{width:950px;height:1200px;overflow:hidden}
body{font-family:"Figtree",sans-serif;color:var(--text);background:var(--white);position:relative}
.topbar{position:absolute;left:0;top:0;width:950px;height:28px;border-bottom:1px solid var(--line);font-size:9px}
.follow{position:absolute;left:104px;top:6px;display:flex;align-items:center;gap:4px}
.follow span{margin-right:6px}
.social{width:17px;height:17px;border:1px solid #d8dadd;display:inline-block}
.call{position:absolute;right:105px;top:7px;display:flex;align-items:center;gap:6px}
.header{position:absolute;left:0;top:28px;width:950px;height:48px;border-bottom:1px solid var(--line)}
.brand{position:absolute;left:104px;top:9px;display:flex;align-items:center;gap:6px;color:var(--ink);font-weight:700;font-size:14px;letter-spacing:.3px}
.brand i{width:28px;height:28px;border-radius:50%;background:var(--ink);display:block}
.nav{position:absolute;right:105px;top:19px;font-size:8px;letter-spacing:1px;color:#59606a;display:flex;gap:8px}
.hero{position:absolute;left:0;top:76px;width:950px;height:348px;
  background:
    radial-gradient(ellipse 150px 190px at 620px 250px,rgba(250,252,252,.95),rgba(250,252,252,0) 70%),
    radial-gradient(ellipse 110px 130px at 600px 110px,rgba(214,160,125,.55),rgba(214,160,125,0) 75%),
    radial-gradient(ellipse 120px 260px at 880px 200px,rgba(40,40,42,.75),rgba(40,40,42,0) 75%),
    radial-gradient(ellipse 160px 120px at 420px 230px,rgba(120,160,90,.45),rgba(120,160,90,0) 75%),
    radial-gradient(ellipse 120px 90px at 250px 70px,rgba(190,205,215,.6),rgba(190,205,215,0) 75%),
    linear-gradient(90deg,#eef1ef 0%,#e6ece6 35%,#d3dfcc 55%,#e9ece6 80%,#b9bdbb 100%)}
.hero-title{position:absolute;left:104px;top:80px;font-size:35px;line-height:42px;font-weight:700;color:var(--ink)}
.hero-sub{position:absolute;left:104px;top:166px;width:340px;font-size:10.5px;line-height:17px;color:#333}
.cta{position:absolute;left:104px;top:213px;width:127px;height:31px;background:var(--teal);color:#fff;font-size:10px;font-weight:500;display:flex;align-items:center;justify-content:center}
.dots{position:absolute;left:104px;top:261px;display:flex;gap:5px}
.dots b{width:7px;height:7px;border-radius:50%;background:#8e9bb0;display:block}
.dots b:first-child{background:none;border:1px solid #8e9bb0}
.tabs{position:absolute;left:0;top:424px;width:950px;height:32px;background:var(--navy);display:flex;padding-left:91px;font-size:8.5px;font-weight:600;letter-spacing:.6px;color:#fff}
.tabs span{padding:0 13px;line-height:32px;position:relative}
.tabs .active{background:#34465c}
.tabs .active::before{content:"";position:absolute;left:50%;top:-5px;margin-left:-5px;border:5px solid transparent;border-top:0;border-bottom-color:var(--navy)}
.services{position:absolute;left:0;top:456px;width:950px;height:276px;background:var(--soft)}
.section-title{position:absolute;font-size:26px;font-weight:400;color:var(--ink);letter-spacing:1.5px;text-align:center}
.service{position:absolute;top:112px;width:160px;text-align:center}
.service svg{display:block;margin:0 auto}
.service h3{font-size:12.5px;font-weight:500;color:#222;margin-top:15px}
.service p{font-size:9.5px;line-height:15px;color:var(--muted);margin-top:6px}
.panel{position:absolute;top:856px;width:361px;height:251px;background:#fff;box-shadow:0 0 10px rgba(0,0,0,.07)}
.thumbs{position:absolute;left:15px;top:25px;display:grid;grid-template-columns:repeat(3,102px);gap:14px 13px}
.thumbs div{height:57px}
.thumbs div:nth-child(1){background:linear-gradient(180deg,#b8cdd6 0%,#8b7f70 45%,#5b3d2e 100%)}
.thumbs div:nth-child(2){background:linear-gradient(180deg,#6e5a44 0%,#a4532e 50%,#3b3330 100%)}
.thumbs div:nth-child(3){background:linear-gradient(180deg,#d9c9a3 0%,#a89770 55%,#5e4b3a 100%)}
.thumbs div:nth-child(4){background:linear-gradient(180deg,#c9d3c8 0%,#8c5a40 55%,#3a2f2c 100%)}
.thumbs div:nth-child(5){background:linear-gradient(180deg,#6f5240 0%,#c2a78a 55%,#e8e3dc 100%)}
.thumbs div:nth-child(6){background:linear-gradient(90deg,#a9aeb3 0%,#cf8a3c 50%,#dcdfe2 100%)}
.thumbs div:nth-child(7){background:linear-gradient(180deg,#b6ad6e 0%,#7a5b40 55%,#34302c 100%)}
.thumbs div:nth-child(8){background:linear-gradient(180deg,#d8d3cb 0%,#8e6a55 55%,#6b3f33 100%)}
.thumbs div:nth-child(9){background:linear-gradient(180deg,#dfe6ee 0%,#b7a998 50%,#8a3e22 100%)}
.mail{position:absolute;left:647px;top:842px;width:36px;height:36px;border-radius:50%;background:#fff;border:1.5px solid var(--ink);display:flex;align-items:center;justify-content:center}
.field{position:absolute;height:28px;border:1px solid #ececec;font-size:8.5px;color:#666;padding-left:11px;line-height:26px}
.field svg{position:absolute;right:10px;top:11px}
.submit{position:absolute;left:610px;top:1058px;width:108px;height:29px;background:var(--teal);color:#fff;font-size:10px;font-weight:500;display:flex;align-items:center;justify-content:center}
.footer{position:absolute;left:0;top:1162px;width:950px;height:38px;background:var(--navy);font-size:8.5px;color:#98a4b3}
.footer .links{position:absolute;left:104px;top:14px;word-spacing:2px}
.footer .copy{position:absolute;right:105px;top:14px}
</style>
</head>
<body>
<div class="topbar">
  <div class="follow"><span>Follow Us on</span><i class="social"></i><i class="social"></i><i class="social"></i></div>
  <div class="call">
    <svg width="9" height="14" viewBox="0 0 9 14"><rect x=".5" y=".5" width="8" height="13" rx="1" fill="none" stroke="#8a9097"/><circle cx="4.5" cy="11" r=".8" fill="#8a9097"/></svg>
    <span>Call Us On&nbsp; 214.555.0142 &nbsp;or&nbsp; 713.555.0187</span>
  </div>
</div>
<div class="header">
  <div class="brand"><i></i>Calloway</div>
  <div class="nav"><span>HOME</span>|<span>PROPERTIES</span>|<span>VIRTUAL TOURS &amp; VIDEOS</span>|<span>PHOTOS</span>|<span>BROKER REFERRALS</span></div>
</div>
<div class="hero" role="img" aria-label="Smiling professional woman seated in a bright office">
  <h1 class="hero-title">Executive Office<br>Solutions.</h1>
  <p class="hero-sub">Come See Why Smarter Companies are Choosing Calloway Business Centers' Dallas, Ft. Worth and Houston Executive Office Suites</p>
  <div class="cta">Get Started Now</div>
  <div class="dots"><b></b><b></b><b></b><b></b><b></b></div>
</div>
<div class="tabs">
  <span class="active">EXECUTIVE OFFICE SUITES</span><span>ON DEMAND MEETING ROOM</span><span>ON DEMAND TRAINING ROOMS</span><span>VIRTUAL OFFICE SOLUTIONS</span><span>VIDEO CONFERENCE SOLUTIONS</span>
</div>
<div class="services">
  <h2 class="section-title" style="left:0;width:950px;top:42px">Our Services</h2>
  <div class="service" style="left:110px">
    <svg width="50" height="48" viewBox="0 0 50 48" aria-label="Paper plane icon" role="img">
      <path d="M20 4L46 16 24 22z" fill="#e9f6fb" stroke="var(--ink)" stroke-width="1.8" stroke-linejoin="round"/>
      <path d="M24 22L20 4 18 16z" fill="var(--ink)"/>
      <path d="M24 22L46 16 26 30z" fill="#fff" stroke="var(--ink)" stroke-width="1.8" stroke-linejoin="round"/>
      <path d="M16 20C4 24 2 38 12 44s20-2 20-8" fill="none" stroke="var(--sky)" stroke-width="1.4" stroke-dasharray="3 3"/>
    </svg>
    <h3>Startups</h3><p>Either you need Dallas/Ft. Worth<br>Office Space</p>
  </div>
  <div class="service" style="left:300px">
    <svg width="50" height="48" viewBox="0 0 50 48" aria-label="Courthouse icon" role="img">
      <path d="M4 12L25 3 46 12z" fill="var(--gold)" stroke="var(--ink)" stroke-width="1.8" stroke-linejoin="round"/>
      <rect x="5" y="12" width="40" height="5" fill="#fff" stroke="var(--ink)" stroke-width="1.8"/>
      <g stroke="var(--ink)" stroke-width="1.8" fill="#fff">
        <rect x="8" y="17" width="5" height="20"/><rect x="16" y="17" width="5" height="20"/><rect x="24" y="17" width="5" height="20"/><rect x="32" y="17" width="5" height="20"/><rect x="39" y="17" width="4" height="20"/>
      </g>
      <rect x="5" y="37" width="40" height="4" fill="var(--gold)" stroke="var(--ink)" stroke-width="1.8"/>
      <rect x="2" y="41" width="46" height="4" fill="#fff" stroke="var(--ink)" stroke-width="1.8"/>
    </svg>
    <h3>Law Firms</h3><p>Either you need Dallas/Ft. Worth<br>Office Space</p>
  </div>
  <div class="service" style="left:490px">
    <svg width="50" height="48" viewBox="0 0 50 48" aria-label="Invoice with coin icon" role="img">
      <path d="M10 3h34v36H10z" fill="#fff" stroke="var(--ink)" stroke-width="1.8" stroke-linejoin="round"/>
      <path d="M10 39c0 5-8 5-8 0V37h8" fill="#dfe5ea" stroke="var(--ink)" stroke-width="1.8" stroke-linejoin="round"/>
      <g stroke="var(--ink)" stroke-width="1.6"><path d="M16 10h22M16 15h22M16 20h16M16 25h12M16 30h10"/></g>
      <circle cx="37" cy="35" r="9" fill="var(--gold)" stroke="var(--ink)" stroke-width="1.8"/>
      <text x="37" y="39.5" text-anchor="middle" font-family="Figtree,sans-serif" font-size="12" font-weight="600" fill="var(--ink)">$</text>
    </svg>
    <h3>Financial</h3><p>Either you need Dallas/Ft. Worth<br>Office Space</p>
  </div>
  <div class="service" style="left:680px">
    <svg width="50" height="48" viewBox="0 0 50 48" aria-label="Graduation cap icon" role="img">
      <path d="M3 18L25 8 47 18 25 28z" fill="var(--ink)" stroke="var(--ink)" stroke-width="1.8" stroke-linejoin="round"/>
      <path d="M12 23v10c0 4 6 7 13 7s13-3 13-7V23l-13 5z" fill="#3c5a86" stroke="var(--ink)" stroke-width="1.8" stroke-linejoin="round"/>
      <path d="M42 20v12" stroke="var(--ink)" stroke-width="1.8"/>
      <circle cx="42" cy="34" r="2.5" fill="var(--gold)" stroke="var(--ink)" stroke-width="1.4"/>
    </svg>
    <h3>Clients</h3><p>Either you need Dallas/Ft. Worth<br>Office Space</p>
  </div>
</div>
<h2 class="section-title" style="left:104px;width:361px;top:788px">Gallery images</h2>
<h2 class="section-title" style="left:484px;width:361px;top:788px">Request information</h2>
<div class="panel" style="left:104px">
  <div class="thumbs" role="img" aria-label="Photos of offices and conference rooms">
    <div></div><div></div><div></div><div></div><div></div><div></div><div></div><div></div><div></div>
  </div>
</div>
<div class="panel" style="left:484px"></div>
<div class="mail"><svg width="20" height="14" viewBox="0 0 20 14"><rect x=".7" y=".7" width="18.6" height="12.6" fill="none" stroke="#2a9bd8" stroke-width="1.3"/><path d="M1 1l9 7 9-7M1 13l7-6M19 13l-7-6" fill="none" stroke="#2a9bd8" stroke-width="1.1"/></svg></div>
<div class="field" style="left:503px;top:907px;width:152px">First Name:</div>
<div class="field" style="left:674px;top:907px;width:152px">Last Name:</div>
<div class="field" style="left:503px;top:942px;width:152px">Company Name:</div>
<div class="field" style="left:674px;top:942px;width:152px">Phone Number:</div>
<div class="field" style="left:503px;top:977px;width:152px">Email:</div>
<div class="field" style="left:674px;top:977px;width:152px">Property Interested In:<svg width="8" height="5" viewBox="0 0 8 5"><path d="M1 1l3 3 3-3" fill="none" stroke="#aaa"/></svg></div>
<div class="field" style="left:503px;top:1012px;width:323px">Product Interested In:<svg width="8" height="5" viewBox="0 0 8 5"><path d="M1 1l3 3 3-3" fill="none" stroke="#aaa"/></svg></div>
<div class="submit">Submit</div>
<div class="footer">
  <div class="links">About Us &nbsp;| &nbsp;Contact Us &nbsp;| &nbsp;Testimonials &nbsp;| &nbsp;FAQs &nbsp;| &nbsp;Careers &nbsp;| &nbsp;Furniture &nbsp;| &nbsp;Specials &nbsp;| &nbsp;Site Map &nbsp;| &nbsp;Privacy</div>
  <div class="copy">Copyright 2016 Calloway Business Centers All Rights Reserved</div>
</div>
</body>
</html>
```